Wordpress web design

We need a website buil in using Wordpress with 5 pages.

Pages: HOME SERVICES GALLERY TESTIMONIALS CONTACT US ABOUT US.

We are looking for a unique, professional and clean web for our construction company.

Company name: TALL OAK BUILDING SERVICES. We can olso provide you with the logo. Please don't use any flashin, intro, or any ready templates.

All your ideas are welcome.

Many thanks,
Dorian

Target Market(s)

Construction

Industry/Entity Type

Construction

Font styles to use
Sans Serif
Decorative

Requirements
Must have
• Connect with construction and London
Nice to have
• Nice and clean

```html
<!DOCTYPE html>
<html lang="en">
<head>
<meta charset="utf-8">
<title>Tall Oak Building Services – Testimonials</title>
<link href="https://fonts.googleapis.com/css2?family=Arvo:wght@400;700&family=Didact+Gothic&display=swap" rel="stylesheet">
<style>
:root{
  --wood:#e6ddd2;
  --wood-dark:#d8cbbd;
  --paper:#ffffff;
  --green:#1f7d06;
  --green-dark:#155c03;
  --green-mid:#2a8b10;
  --ink:#2b2b2b;
  --muted:#555555;
  --rule:#cfcfcf;
  --crumb:#f0f0f0;
  --cal-line:#d6d6d6;
  --cal-text:#a9a9a9;
  --footer-text:#f2e98a;
  --footer-head:#f4f4f4;
}
*{box-sizing:border-box;margin:0;padding:0}
html,body{width:1200px;height:986px;overflow:hidden}
body{
  position:relative;
  font-family:"Arvo",Georgia,serif;
  color:var(--ink);
  background:linear-gradient(90deg,var(--wood) 0%,var(--wood-dark) 18%,var(--wood) 40%,var(--wood-dark) 65%,var(--wood) 85%,var(--wood-dark) 100%);
}
.page{position:absolute;left:118px;top:16px;width:986px;height:970px;background:var(--paper);box-shadow:0 0 10px rgba(0,0,0,.25)}
.topbar{position:absolute;left:0;top:0;width:986px;height:41px;background:var(--green)}
.topbar .notch{position:absolute;left:467px;top:41px}
.social{position:absolute;left:15px;top:10px;display:flex;gap:7px}
.social span{width:20px;height:20px;border-radius:50%;background:#cfe3c6}
.logo{position:absolute;left:54px;top:80px;font-family:"Didact Gothic",Arial,sans-serif;font-size:38px;letter-spacing:2px;color:#111}
.phone{position:absolute;right:20px;top:70px;display:flex;align-items:center;gap:14px;font-size:16px;font-weight:700;color:#333}
.nav{position:absolute;left:20px;top:161px;width:946px;height:42px;border-top:1px dashed var(--rule);border-bottom:1px dashed var(--rule);display:flex;align-items:center}
.nav a{font-size:14px;color:#333;text-decoration:none;padding:0 22px;border-right:1px solid var(--rule);line-height:24px}
.nav a:last-child{border-right:0}
.nav a.active{background:var(--green);color:#fff;line-height:34px;border:0;margin-right:0}
.crumb{position:absolute;left:20px;top:238px;width:947px;height:42px;border:1px solid var(--rule);padding:3px}
.crumb div{height:100%;background:var(--crumb);font-size:18px;line-height:34px;padding-left:12px;color:#333}
.testimonial{position:absolute;left:20px;width:600px;display:flex;gap:20px}
.avatar{width:110px;height:110px;border:1px solid var(--rule);padding:5px;background:#fff;box-shadow:0 1px 2px rgba(0,0,0,.1)}
.avatar div{width:100%;height:100%}
.t-name{font-size:20px;margin-top:2px;color:#222}
.t-text{font-size:13px;color:var(--muted);margin-top:4px}
.calendar{position:absolute;left:726px;top:296px;width:233px}
.calendar h4{font-size:11px;font-weight:400;text-align:center;margin-bottom:6px;color:#333}
.calendar table{width:100%;border-collapse:collapse;font-size:12px;table-layout:fixed}
.calendar th,.calendar td{border:1px solid var(--cal-line);height:24px;text-align:center;color:var(--cal-text);font-weight:400}
.calendar th{background:#e4e4e4;color:#fff}
.calendar td.today{color:#222}
.calendar td.past{color:#8fb488}
.footer{position:absolute;left:0;top:790px;width:986px;height:180px;background:linear-gradient(90deg,var(--green-dark) 0%,#1a6d04 35%,var(--green-mid) 50%,#1b6b05 70%,var(--green-dark) 100%)}
.f-col{position:absolute;top:30px}
.f-col h3{font-size:19px;color:var(--footer-head);padding-bottom:14px;border-bottom:1px solid rgba(255,255,255,.18);width:220px}
.f-col p{font-size:13px;line-height:20px;color:var(--footer-text);margin-top:14px;width:210px}
.f-col ul{list-style:none;margin-top:16px;font-size:13px;line-height:21px;color:var(--footer-text)}
.f-col li::before{content:"•";color:#fff;margin-right:8px}
.search{position:absolute;left:747px;top:24px;width:182px;height:32px;display:flex;border:1px solid #0c3f02}
.search span{flex:1;background:#0f4a03;color:#fff;font-size:12px;line-height:30px;padding-left:10px;font-family:Arial,sans-serif}
.search i{width:36px;background:#0a3602;display:flex;align-items:center;justify-content:center}
</style>
</head>
<body>
<div class="page">
  <header class="topbar">
    <div class="social"><span></span><span></span><span></span><span></span></div>
    <svg class="notch" width="14" height="9"><polygon points="0,0 14,0 7,9" fill="#1f7d06"/></svg>
  </header>
  <div class="logo">Your logo</div>
  <div class="phone">
    <svg width="16" height="26" viewBox="0 0 16 26"><rect x="1" y="1" width="14" height="24" rx="2" fill="none" stroke="#777" stroke-width="2"/><circle cx="8" cy="21" r="1.5" fill="#777"/></svg>
    Call 24 Hours. 1.888.555.0192
  </div>
  <nav class="nav">
    <a href="#">Home</a><a href="#">SERVICES</a><a href="#">GALLERY</a><a class="active" href="#">TESTIMONIALS</a><a href="#">CONTACT US</a><a href="#">ABOUT US</a>
  </nav>
  <div class="crumb"><div>TESTIMONIALS &nbsp;»</div></div>

  <div class="testimonial" style="top:328px">
    <div class="avatar"><div role="img" aria-label="Photo of a hand with handwritten text" style="background:linear-gradient(135deg,#3a2a20,#a86a4a,#2a1d16)"></div></div>
    <div><div class="t-name">Mr.Harlow</div><div class="t-text">BEST TALL OAK BUILDING SERVICES.</div></div>
  </div>
  <div class="testimonial" style="top:484px">
    <div class="avatar"><div role="img" aria-label="Portrait photo of a client" style="background:linear-gradient(135deg,#5b6fc4,#3a2a28,#c27a8e)"></div></div>
    <div><div class="t-name">Brenna</div><div class="t-text">BEST TALL OAK BUILDING SERVICES.</div></div>
  </div>
  <div class="testimonial" style="top:640px">
    <div class="avatar"><div role="img" aria-label="Portrait photo of a client" style="background:linear-gradient(135deg,#d9dcd8,#b08a70,#6a7a88)"></div></div>
    <div><div class="t-name">Callum</div><div class="t-text">BEST TALL OAK BUILDING SERVICES.</div></div>
  </div>

  <div class="calendar">
    <h4>MARCH 2015</h4>
    <table>
      <tr><th>M</th><th>T</th><th>W</th><th>T</th><th>F</th><th>S</th><th>S</th></tr>
      <tr><td></td><td></td><td></td><td></td><td></td><td></td><td>1</td></tr>
      <tr><td>2</td><td>3</td><td>4</td><td>5</td><td>6</td><td>7</td><td>8</td></tr>
      <tr><td>9</td><td>10</td><td>11</td><td>12</td><td>13</td><td class="today">14</td><td>15</td></tr>
      <tr><td>16</td><td>17</td><td>18</td><td>19</td><td>20</td><td>21</td><td>22</td></tr>
      <tr><td>23</td><td>24</td><td>25</td><td>26</td><td>27</td><td>28</td><td>29</td></tr>
      <tr><td class="past">30</td><td class="past">31</td><td colspan="5"></td></tr>
      <tr><td colspan="3"></td><td></td><td colspan="3"></td></tr>
    </table>
  </div>

  <footer class="footer">
    <div class="f-col" style="left:20px">
      <h3>About Company</h3>
      <p>We are construction partners who are passionate about what we do and our partners' success.</p>
    </div>
    <div class="f-col" style="left:268px">
      <h3>Archives Widget</h3>
      <ul><li>January 2010</li><li>December 2009</li><li>November 2009</li><li>October 2009</li><li>Life &amp; Style</li></ul>
    </div>
    <div class="f-col" style="left:507px">
      <h3>Categories</h3>
      <ul><li>Entertainment</li><li>Technology</li><li>Template Design</li><li>Sports &amp; Recreation</li><li>Life &amp; Style</li></ul>
    </div>
    <div class="search"><span>Search</span><i><svg width="12" height="12" viewBox="0 0 12 12"><circle cx="5" cy="5" r="3.5" fill="none" stroke="#fff" stroke-width="1.6"/><line x1="7.5" y1="7.5" x2="11" y2="11" stroke="#fff" stroke-width="1.8"/></svg></i></div>
  </footer>
</div>
</body>
</html>
```